Varga Lillas Physiotherapy Business Card Vienna

We need a business card design for a newly created Physiotherapy company based in Vienna Austria.
We seek a simple, modern, minimalist design without too much color variation. The font should look young/fresh, but definitely not childish or so. Since we are a starting Business, we currently haven't got a logo, if you feel like a logo would fit your design, feel free to use one, but it's not necessary.
Target Market(s)
Healthcare, young and elderly people with mobility issues
Industry/Entity Type
Health And Wellness
Contact Information for Business Card
Name: Lilla Varga
Title description: Physiotherapist
Phone num: +43 664 5290 4816
e-mail: lilla.praxis@brelomail.com
Colors
Designer to choose colors to be used in the design.
Requirements
Must have
- Final design language must be in German, basically, the Title Description needs to be "Physiotherapeutin" the other details remain as in the English Language.
Nice to have
- Simple, modern, minimalist design
Should not have
- too many colors, Obvious use of a skeleton, skull, spline

```html
<!DOCTYPE html>
<html lang="de">
<head>
<meta charset="utf-8">
<title>Varga Lillas Physiotherapy – Business Card</title>
<link href="https://fonts.googleapis.com/css2?family=Lato:wght@400;700;900&display=swap" rel="stylesheet">
<style>
  :root {
    --backdrop: #2b2b2b;
    --card: #1c1c1c;
    --gloss: #4a4a4a;
    --gloss-light: #6a6a6a;
    --ink: #f2f2f2;
    --ink-soft: #d9d9d9;
    --accent-line: #ffffff;
  }
  * { margin: 0; padding: 0; box-sizing: border-box; }
  html, body {
    width: 1200px;
    height: 895px;
    overflow: hidden;
    background: var(--backdrop);
    font-family: "Lato", sans-serif;
  }
  .canvas {
    width: 1200px;
    height: 895px;
    display: flex;
    flex-direction: column;
    align-items: center;
    justify-content: center;
    gap: 40px;
  }
  .card {
    position: relative;
    width: 560px;
    height: 320px;
    background: var(--card);
    box-shadow: 0 18px 40px rgba(0,0,0,0.55);
    overflow: hidden;
  }
  /* Front */
  .card--front {
    display: flex;
    flex-direction: column;
    align-items: center;
    justify-content: center;
  }
  .brand-name {
    font-weight: 700;
    font-size: 44px;
    letter-spacing: 1px;
    color: var(--gloss);
    text-transform: uppercase;
    line-height: 1;
  }
  .brand-tagline {
    margin-top: 8px;
    font-weight: 400;
    font-size: 22px;
    letter-spacing: 9px;
    color: var(--gloss);
    text-transform: uppercase;
    padding-left: 9px;
  }
  /* Back */
  .card--back {
    display: flex;
    align-items: center;
    justify-content: center;
    padding-bottom: 10px;
  }
  .identity {
    text-align: right;
    color: var(--ink);
  }
  .identity__name {
    font-weight: 900;
    font-size: 22px;
    letter-spacing: 0.5px;
    text-transform: uppercase;
    line-height: 1.05;
  }
  .identity__title {
    font-size: 14px;
    color: var(--ink-soft);
  }
  .divider {
    width: 1.5px;
    height: 46px;
    background: var(--ink);
    margin: 0 20px;
  }
  .contact {
    list-style: none;
    color: var(--ink);
    font-size: 14px;
    line-height: 1.7;
  }
  .contact__item {
    display: flex;
    align-items: center;
    gap: 10px;
  }
  .contact__icon {
    width: 13px;
    height: 13px;
    flex: none;
  }
  .card__edge-line {
    position: absolute;
    left: 0;
    right: 0;
    bottom: 0;
    height: 5px;
    background: var(--accent-line);
  }
</style>
</head>
<body>
  <main class="canvas">
    <section class="card card--front" aria-label="Kartenvorderseite">
      <div class="brand-name">Varga Lillas</div>
      <div class="brand-tagline">Physiotherapy</div>
    </section>

    <section class="card card--back" aria-label="Kartenrückseite">
      <div class="identity">
        <div class="identity__name">Lilla Varga</div>
        <div class="identity__title">Physiotherapeutin</div>
      </div>
      <div class="divider"></div>
      <ul class="contact">
        <li class="contact__item">
          <svg class="contact__icon" viewBox="0 0 14 14" aria-hidden="true">
            <rect x="3.5" y="0.8" width="7" height="12.4" rx="1.4" fill="none" stroke="#f2f2f2" stroke-width="1.3"/>
            <line x1="6" y1="11" x2="8" y2="11" stroke="#f2f2f2" stroke-width="1.2"/>
          </svg>
          <span>+43 664 5290 4816</span>
        </li>
        <li class="contact__item">
          <svg class="contact__icon" viewBox="0 0 14 14" aria-hidden="true">
            <rect x="1" y="3" width="12" height="8.5" fill="none" stroke="#f2f2f2" stroke-width="1.3"/>
            <polyline points="1,3.5 7,8 13,3.5" fill="none" stroke="#f2f2f2" stroke-width="1.3"/>
          </svg>
          <span>lilla.praxis@brelomail.com</span>
        </li>
      </ul>
      <div class="card__edge-line"></div>
    </section>
  </main>
</body>
</html>
```